Unternehmensbroschüre für Personaldienstleister
Die Zusammenarbeit mit Annika war sehr produktiv und angenehm. Sie ist sehr professionell, kreativ und konnte unsere Vorstellungen super umsetzen. Auf jeden Fall weiter zu empfehlen!
Zielgruppe
Weidmann & Kollegen ist führend in der schnellen Bereitstellung von Spezialisten und Teams für anspruchsvolle ICT und Business Projekte. Beginnend beim Bereitstellen eines einzelnen erfolgskritischen Fachspezialisten, bis hin zum Einsatz einer gesamten Projekt-Taskforce, sichern wir den Erfolg unserer Kunden in der digitalen Zukunft.
Seit über 25 Jahren sind wir erfolgreich im Personalverleih von IT-Spezialisten tätig und haben uns ein grosses Know-how in den Branchen Banken, Versicherungen und öffentliche Hand aufgebaut.
Aufgabenstellung
Wir sind Personaldienstleister und benötigen eine Unternehmensbroschüre in unserem Corporate Design (PDF und InDesign). Das Corporate Design ist auf die Broschüre anzuwenden. Im Anhang finden Sie Dateien zum Corporate Design (Schrift, Logo, Claim, Farbwerte und Manual).
Die Broschüre soll im A4 Format erstellt werden und 12 Seiten beinhalten.
Es gibt einen ersten Entwurf vom Texter sowie ein grobe Richtung, wie die Seiten verteilt werden soll. Dieser ist im Anhang beigefügt. kann jedoch noch angepasst werden. Auch die Verteilung der Seiten soll eine grobe Richtung vorgeben und kann individuell angepasst werden. Uns ist wichtig, dass die Bilder/ Graphiken Emotionen wecken und die textlichen Bausteine diese unterstützen. Der Text sollte nicht zu lang sein und ein gutes Verhältnis zu den Bildern darstellen.
Bei den Fotos können Sie Vorschläge aus Fotodatenbanken machen (optimalerweise aus Lumora Bildpool).
Ein Beispiel welches uns gut gefällt ist die Broschüre von dem Unternehmen Tempokraftwerk (siehe Anhang). Es bietet ein gutes Verhältnis zwischen Bilder, Icons und Text. Auf den Seiten 8-11 werden mit der Bildersprache (Berg, Holz ) die Aussagen entsprechend unterstützt.

```html
<!DOCTYPE html>
<html lang="de">
<head>
<meta charset="utf-8">
<title>Unternehmensbroschüre – Was uns ausmacht</title>
<link rel="stylesheet" href="https://fonts.googleapis.com/css2?family=Mulish:wght@300;400;800;900&display=swap">
<style>
  :root {
    --bg: #e6e6e6;
    --paper: #f7f7f7;
    --ink: #2b2b2b;
    --ink-soft: #555a5e;
    --accent: #5b9bd5;
    --accent-deep: #4a86c4;
    --green: #5aae84;
    --rule: #9a9a9a;
    --photo-cool: #9fb0c2;
    --photo-mid: #c9d2dc;
    --photo-warm: #f2e6cf;
  }
  * { box-sizing: border-box; margin: 0; padding: 0; }
  html, body {
    width: 1200px; height: 848px; overflow: hidden;
    background: var(--bg);
    font-family: "Mulish", Arial, sans-serif;
    color: var(--ink);
  }
  .spread {
    position: absolute; left: 50px; top: 35px;
    width: 1100px; height: 778px;
    display: flex;
    box-shadow: 0 6px 24px rgba(0,0,0,.12);
  }
  .page {
    position: relative; width: 550px; height: 778px;
    background: var(--paper); overflow: hidden;
  }
  .page--left { background: linear-gradient(to right, var(--paper) 88%, #e9e9e9); }
  .page--right { background: linear-gradient(to left, var(--paper) 90%, #e6e6e6); }

  .photo {
    position: absolute; top: 0;
    background:
      radial-gradient(ellipse at 85% 30%, var(--photo-warm) 0%, rgba(242,230,207,0) 55%),
      linear-gradient(160deg, var(--photo-mid) 0%, var(--photo-cool) 55%, #7f92a8 100%);
  }
  .photo--left { left: 0; width: 550px; height: 490px; }
  .photo--right {
    left: 0; width: 225px; height: 440px;
    background:
      radial-gradient(ellipse at 40% 25%, var(--photo-warm) 0%, rgba(242,230,207,0) 70%),
      linear-gradient(180deg, #e3e1dc 0%, #c7ced6 100%);
  }

  .claim {
    position: absolute; left: 36px; top: 520px;
    writing-mode: vertical-rl; transform: rotate(180deg);
    font-size: 9px; font-weight: 900; letter-spacing: .06em;
    text-transform: uppercase; height: 150px; text-align: left;
  }
  .folio {
    position: absolute; font-size: 8px; font-weight: 400; color: var(--ink-soft);
  }
  .folio--left { left: 36px; bottom: 96px; }
  .folio-rule--left {
    position: absolute; left: 36px; bottom: 112px; width: 80px; height: 1px; background: var(--rule);
  }
  .deco {
    position: absolute; left: 150px; top: 620px; width: 260px; height: 260px;
  }

  .kicker {
    position: absolute; right: 40px; top: 150px;
    font-size: 8px; font-weight: 800; letter-spacing: .05em; text-transform: uppercase;
  }
  .content {
    position: absolute; left: 258px; top: 200px; width: 250px;
  }
  .headline {
    font-size: 25px; line-height: 1.05; font-weight: 900;
    color: var(--accent); text-transform: uppercase; letter-spacing: .01em;
    margin-bottom: 18px;
  }
  .body p {
    font-size: 11px; line-height: 1.45; font-weight: 300;
    color: var(--ink-soft); margin-bottom: 10px;
  }
  .body p.lead-out { font-weight: 800; color: var(--ink); }

  .folio-rule--right-v {
    position: absolute; right: 70px; bottom: 60px; width: 1px; height: 110px; background: var(--rule);
  }
  .folio-rule--right-h {
    position: absolute; right: 40px; bottom: 60px; width: 80px; height: 1px; background: var(--rule);
  }
  .folio--right { right: 100px; bottom: 44px; }
</style>
</head>
<body>
  <main class="spread">
    <section class="page page--left">
      <div class="photo photo--left" role="img" aria-label="Foto: fröhliche Kolleginnen und Kollegen fahren im hellen Loft-Büro auf blauen Bürostühlen um die Wette"></div>
      <div class="claim">Digital. Business. People.</div>
      <div class="folio-rule--left"></div>
      <div class="folio folio--left">04</div>
      <svg class="deco" viewBox="0 0 260 260" aria-hidden="true">
        <defs>
          <linearGradient id="decoGrad" x1="0" y1="0" x2="1" y2="1">
            <stop offset="0" stop-color="var(--accent-deep)"/>
            <stop offset="1" stop-color="var(--green)"/>
          </linearGradient>
        </defs>
        <circle cx="130" cy="130" r="128" fill="url(#decoGrad)" opacity=".85"/>
      </svg>
    </section>

    <section class="page page--right">
      <div class="photo photo--right" role="img" aria-label="Fortsetzung des Fotos: helles Büro mit Fensterfront und einfallendem Sonnenlicht"></div>
      <div class="kicker">– Was uns ausmacht</div>
      <article class="content">
        <h1 class="headline">Auch die<br>„Soft-Skills“<br>sind gefragt.</h1>
        <div class="body">
          <p>Wir könnten Ihnen jetzt viel über uns erzählen und einen Bulletpoint nach dem anderen aufreihen. Tun wir aber nicht.</p>
          <p>Dass wir seit über 25 Jahren erfolgreich im Personalverleih von IT-Spezialisten tätig sind, haben wir Ihnen schon verraten.</p>
          <p>Und dass wir viele grosse Unternehmen unter anderem aus den Bereichen Banken, Versicherungen, Health-Care und öffentliche Hand zu unseren Kunden zählen, haben Sie sicherlich schon gehört.</p>
          <p class="lead-out">Doch statt dem typischen Buzzword-Bingo wollten wir Ihnen an dieser Stelle etwas über uns erzählen, was unsere Kunden an uns besonders schätzen.</p>
        </div>
      </article>
      <div class="folio-rule--right-v"></div>
      <div class="folio-rule--right-h"></div>
      <div class="folio folio--right">05</div>
    </section>
  </main>
</body>
</html>
```